Health Supplement Series for 60 tablets of pure Gold Petal Grain powder

We need a packaging design theme for a health supplement for international consumers. Our initial product is called 'Gold Petal Grain'. It is for general health and is particularly effective for diabetic symptoms.
We would like to see designs that are clean and fresh.
It should give the impression of professional, premium pharmaceutical grade products.
Our company logo is attached below.

Target Market(s)

International

Industry/Entity Type

Health And Wellness

Font styles to use
Serif
Sans Serif

Requirements
Must have
• Bottle and box packaging required.
• 1st product is bottle of 60 tablets of 0.5gm each.
Should not have
• Seals and other "must buy" "guaranteed" etc

```html
<!DOCTYPE html>
<html lang="en">
<head>
<meta charset="utf-8">
<title>Gold Petal Grain Supplement Label</title>
<link rel="stylesheet" href="https://fonts.googleapis.com/css2?family=Open+Sans:wght@300;700&family=Encode+Sans+Condensed:wght@300&family=Montserrat:wght@600&display=swap">
<style>
  :root {
    --leaf-dark: #3f9a2a;
    --leaf-mid: #7cc43c;
    --leaf-light: #d9f2a8;
    --title-green: #2f8a2a;
    --brand-green: #4a8f34;
    --accent-red: #e8141b;
    --caption-grey: #8a8a8a;
    --paper: #ffffff;
  }
  html, body {
    margin: 0;
    padding: 0;
    width: 1133px;
    height: 1200px;
    overflow: hidden;
    background: var(--paper);
  }
  .label {
    position: relative;
    width: 1133px;
    height: 1200px;
    overflow: hidden;
    background: var(--paper);
  }
  .foliage {
    position: absolute;
    left: 0;
    top: 0;
    width: 1133px;
    height: 1150px;
    background:
      linear-gradient(to bottom, rgba(255,255,255,0) 0%, rgba(255,255,255,0) 60%, rgba(255,255,255,0.85) 82%, var(--paper) 100%),
      radial-gradient(ellipse 420px 520px at 420px 380px, var(--leaf-light) 0%, rgba(200,235,140,0.7) 45%, rgba(124,196,60,0) 100%),
      radial-gradient(ellipse 380px 600px at 980px 420px, var(--leaf-dark) 0%, rgba(63,154,42,0.6) 55%, rgba(63,154,42,0) 100%),
      radial-gradient(ellipse 260px 420px at 60px 300px, var(--leaf-mid) 0%, rgba(124,196,60,0) 100%),
      linear-gradient(135deg, #a8da6a 0%, #c9ec92 40%, #8fcb4f 75%, #5aac34 100%);
  }
  .brand {
    position: absolute;
    left: 190px;
    top: 262px;
    display: flex;
    align-items: center;
    gap: 18px;
  }
  .brand-mark {
    width: 58px;
    height: 58px;
    background: var(--brand-green);
  }
  .brand-name {
    font-family: "Montserrat", sans-serif;
    font-weight: 600;
    font-size: 46px;
    letter-spacing: 4px;
    color: var(--brand-green);
    line-height: 1;
  }
  .product-name {
    position: absolute;
    left: 182px;
    top: 391px;
    margin: 0;
    font-family: "Open Sans", sans-serif;
    font-weight: 300;
    font-size: 185px;
    line-height: 176px;
    letter-spacing: -5px;
    color: var(--title-green);
  }
  .product-name span { display: block; }
  .product-type {
    position: absolute;
    left: 197px;
    top: 962px;
    font-family: "Open Sans", sans-serif;
    font-weight: 700;
    font-size: 50px;
    letter-spacing: -1px;
    color: var(--accent-red);
    line-height: 1;
  }
  .benefits {
    position: absolute;
    left: 195px;
    top: 1040px;
    margin: 0;
    font-family: "Encode Sans Condensed", sans-serif;
    font-weight: 300;
    font-size: 38px;
    line-height: 56px;
    color: var(--caption-grey);
  }
</style>
</head>
<body>
<main class="label">
  <div class="foliage" role="img" aria-label="Backlit fresh green ginkgo leaves on soft light background"></div>

  <div class="brand">
    <div class="brand-mark"></div>
    <div class="brand-name">VERDANE HEALTH</div>
  </div>

  <h1 class="product-name">
    <span>Gold</span>
    <span>Petal</span>
    <span>Grain</span>
  </h1>

  <div class="product-type">SUPPLEMENT</div>
  <p class="benefits">effective for diabetic symptoms<br>general health</p>
</main>
</body>
</html>
```